P&H RESTORATION

I want a brochure similiar to the example i've attached.
My company name is P&H Restoration. The website is: P-H-Restoration.com.
The phone number is 803.417.9056.

I don't like the "yellow" being the main color of the example so I'm open to suggestions. I want something CLEAN & Simple, like our logo . This will be a bi fold brochure

```html
<!DOCTYPE html>
<html lang="en">
<head>
<meta charset="utf-8">
<title>P&amp;H Restoration — Bi-fold Brochure</title>
<link rel="stylesheet" href="https://fonts.googleapis.com/css2?family=Montserrat:wght@300;400;500;600;700&display=swap">
<style>
  :root {
    --sky: #16b2ea;
    --sky-deep: #0aa6e0;
    --sky-pale: #cdeefb;
    --orange: #f28c00;
    --white: #ffffff;
    --navy: #0d1f33;
    --paper: #ffffff;
    --gap: #f3f3f3;
  }
  * { box-sizing: border-box; margin: 0; padding: 0; }
  html, body { width: 869px; height: 1200px; overflow: hidden; background: var(--paper); }
  body { font-family: "Montserrat", Arial, sans-serif; color: var(--white); position: relative; }

  .gap-band { position: absolute; left: 0; top: 596px; width: 869px; height: 14px; background: var(--gap); }

  .spread { position: absolute; left: 33px; width: 803px; overflow: hidden; }
  .spread--outside { top: 32px; height: 563px; }
  .spread--inside { top: 610px; height: 558px; }

  .panel { position: absolute; top: 0; height: 100%; width: 401.5px; overflow: hidden; }
  .panel--left { left: 0; }
  .panel--right { left: 401.5px; }

  .fill { position: absolute; inset: 0; }
  .blueprint-back { background: radial-gradient(ellipse at 70% 40%, #3cc3f0 0%, var(--sky) 55%, #10a9e3 100%); }
  .blueprint-cover { background: linear-gradient(160deg, #22b9ee 0%, var(--sky) 60%, #14afe8 100%); }
  .flood-photo { background: linear-gradient(180deg, #e9f1f7 0%, #d3dde4 35%, #b9a58a 55%, #7fa3bd 75%, #4f7fa3 100%); }
  .text-panel-bg { background: linear-gradient(180deg, #1ab3ea 0%, #18ade3 70%, #1596c9 100%); }

  svg.shapes { position: absolute; inset: 0; }

  /* Company name, set as plain text */
  .company-name { position: absolute; color: var(--white); font-weight: 500; white-space: nowrap; letter-spacing: 1px; }
  .company-name--back { left: 0; width: 367px; text-align: center; top: 268px; font-size: 27px; }
  .company-name--cover { left: 139px; width: 263px; text-align: center; top: 334px; font-size: 23px; }
  .company-name--footer { left: 21px; top: 513px; font-size: 11px; letter-spacing: .6px; }

  .ribbon { position: absolute; background: var(--orange); color: var(--white); display: flex; align-items: center; }
  .ribbon--claims { left: 0; top: 360px; width: 367px; height: 21px;
    clip-path: polygon(0 0, 100% 0, 94% 100%, 0 100%);
    font-size: 13px; font-weight: 700; letter-spacing: 3.3px; padding-left: 55px; }
  .ribbon--motto { left: 139px; top: 402px; width: 263px; height: 12px;
    clip-path: polygon(2% 0, 100% 0, 100% 100%, 0 100%);
    font-size: 7.2px; font-weight: 600; letter-spacing: 2.2px; padding-left: 18px; }

  .contact { position: absolute; left: 76px; top: 390px; display: flex; align-items: center; gap: 7px;
    font-size: 10px; font-weight: 600; }
  .contact__item { display: flex; align-items: center; gap: 3px; }
  .contact__item svg { width: 10px; height: 10px; }

  .cover-web { position: absolute; right: 21px; top: 532px; display: flex; align-items: center; gap: 3px;
    font-size: 13px; font-weight: 700; }
  .cover-web svg { width: 11px; height: 11px; }

  .motto-stack { position: absolute; left: 190px; top: 360px; width: 225px; text-align: center;
    font-weight: 400; font-size: 25px; letter-spacing: 2px; line-height: 31px; }
  .motto-stack__line { display: block; }
  .motto-stack__line--dark { color: var(--navy); }
  .rule { position: absolute; height: 1px; background: var(--navy); }
  .rule--one { left: 226px; top: 392px; width: 176px; }
  .rule--two { left: 198px; top: 425px; width: 184px; }

  .copy { position: absolute; left: 29px; top: 16px; width: 345px; font-size: 8.1px; font-weight: 400;
    line-height: 9.7px; letter-spacing: .55px; text-align: justify; color: var(--white); }
  .copy p + p { margin-top: 10px; }

  .tagline { position: absolute; left: 153px; top: 521px; font-size: 7.5px; font-weight: 700;
    letter-spacing: 1.3px; color: var(--white); white-space: nowrap; }
</style>
</head>
<body>
  <div class="gap-band"></div>

  <section class="spread spread--outside">
    <div class="panel panel--left">
      <div class="fill blueprint-back" role="img" aria-label="Rolled architectural blueprints tinted in bright blue"></div>
      <div class="company-name company-name--back">P&amp;H Restoration</div>
      <div class="ribbon ribbon--claims">Insurance Claim Specialist</div>
      <div class="contact">
        <span class="contact__item">
          <svg viewBox="0 0 24 24"><path fill="#f28c00" d="M6.6 10.8a15 15 0 0 0 6.6 6.6l2.2-2.2a1 1 0 0 1 1-.25 11.4 11.4 0 0 0 3.6.6 1 1 0 0 1 1 1V20a1 1 0 0 1-1 1A17 17 0 0 1 3 4a1 1 0 0 1 1-1h3.5a1 1 0 0 1 1 1c0 1.25.2 2.45.6 3.6a1 1 0 0 1-.25 1z"/></svg>
          803.417.9056
        </span>
        <span class="contact__item">
          <svg viewBox="0 0 24 24" fill="none" stroke="#f28c00" stroke-width="2.4"><circle cx="12" cy="12" r="9.5"/><path d="M2.5 12h19M12 2.5c3 3 3 16 0 19M12 2.5c-3 3-3 16 0 19"/></svg>
          P-H-Restoration.com
        </span>
      </div>
    </div>

    <div class="panel panel--right">
      <div class="fill blueprint-cover" role="img" aria-label="Faint floor-plan drawing tinted in blue"></div>
      <svg class="shapes" viewBox="0 0 401.5 563" preserveAspectRatio="none">
        <polygon points="0,0 217,113 5,563 0,563" fill="#cdeefb" role="img" aria-label="Rolled blueprints in pale light"/>
        <polyline points="2,0 217,113 5,563" fill="none" stroke="#f28c00" stroke-width="4"/>
      </svg>
      <div class="company-name company-name--cover">P&amp;H Restoration</div>
      <div class="ribbon ribbon--motto">BULID - RENOVATE - RESTORE</div>
      <div class="cover-web">
        <svg viewBox="0 0 24 24" fill="none" stroke="#f28c00" stroke-width="2.4"><circle cx="12" cy="12" r="9.5"/><path d="M2.5 12h19M12 2.5c3 3 3 16 0 19M12 2.5c-3 3-3 16 0 19"/></svg>
        P-H-Restoration.com
      </div>
    </div>
  </section>

  <section class="spread spread--inside">
    <div class="panel panel--left">
      <div class="fill flood-photo" role="img" aria-label="Bright modern kitchen with floodwater covering the floor"></div>
      <svg class="shapes" viewBox="0 0 401.5 558" preserveAspectRatio="none">
        <polygon points="395,0 401.5,0 401.5,558 191,440" fill="#0aa6e0"/>
      </svg>
      <div class="motto-stack">
        <span class="motto-stack__line">BUILD</span>
        <span class="motto-stack__line motto-stack__line--dark">RENOVATE</span>
        <span class="motto-stack__line">RESTORE</span>
      </div>
      <div class="rule rule--one"></div>
      <div class="rule rule--two"></div>
    </div>

    <div class="panel panel--right">
      <div class="fill text-panel-bg" role="img" aria-label="Faded flooded interior tinted in blue"></div>
      <div class="copy">
        <p>Lorem ipsum dolor sit amet, consectetuer adipiscing elit, sed diam nonummy nibh euismod tincidunt ut laoreet dolore magna aliquam erat volutpat. Ut wisi enim ad minim veniam, quis nostrud exerci tation ullamcorper suscipit lobortis nisl ut aliquip ex ea commodo consequat. Duis autem vel eum iriure dolor in hendrerit in vulputate velit esse molestie consequat, vel illum dolore eu feugiat nulla facilisis at vero eros et accumsan et iusto odio dignissim qui blandit praesent luptatum zzril delenit augue duis dolore te feugait nulla facilisi.</p>
        <p>Lorem ipsum dolor sit amet, cons ectetuer adipiscing elit, sed diam nonummy nibh euismod tincidunt ut laoreet dolore magna aliquam erat volutpat. Ut wisi enim ad minim veniam, quis nostrud exerci tation ullamcorper suscipit lobortis nisl ut aliquip ex ea commodo consequat.</p>
        <p>Lorem ipsum dolor sit amet, consectetuer adipiscing elit, sed diam nonummy nibh euismod tincidunt ut laoreet dolore magna aliquam erat volutpat. Ut wisi enim ad minim veniam, quis nostrud exerci tation ullamcorper suscipit lobortis nisl ut aliquip ex ea commodo consequat. Duis autem vel eum iriure dolor in hendrerit in vulputate velit esse molestie consequat, vel illum dolore eu feugiat nulla facilisis at vero eros et accumsan et iusto odio dignissim qui blandit praesent luptatum zzril delenit augue duis dolore te feugait nulla facilisi.</p>
      </div>
      <svg class="shapes" viewBox="0 0 401.5 558" preserveAspectRatio="none">
        <polygon points="58,256 401.5,256 401.5,498 131,498" fill="#8fb3c9" role="img" aria-label="Open-plan kitchen and dining area flooded with dark water"/>
        <line x1="56" y1="256" x2="129" y2="498" stroke="#f28c00" stroke-width="5"/>
      </svg>
      <div class="company-name company-name--footer">P&amp;H Restoration</div>
      <div class="tagline">HERE FOR YOU, EVERY STEP OF THE WAY.</div>
    </div>
  </section>
</body>
</html>
```